ONE PAGE WEB DESIGN NEEDED for Finance Company

We need a web design (ONE PAGE DESIGN ONLY) for a new finance website called Brightwell Lending. Brightwell Lending helps customers get the right loan, whether its a home loan, investment loan, business loan etc.

You are required to come up with just the homepage design. Professionalism and quality is the key factors in the successful design.

Here are a few design questions to help you out:

-
What information should be used on the page?
Ive provided a document which outlines all the information needed to put on homepage (attached to the brief - called brightwell_page_info). Also see the Must Have section below on this brief.

-
What links should appear in the navigation/footer?:
The navigation should provide links to the following pages (NOTE: services link has subcategories):
1 Homepage
2 Services
- Home loans
- Investment loans
- Refinancing loans
- Business loans
3 About Us
4 FAQ
5 Contact Us

-
What colors should be used in the design?
Our company colors - Cyan: #2EADE3, Blue: #004B70, White. Feel free to submit designs with slight variations if you feel it improves the design.

-
What should the layout of the page be?
This is up to you to come up with - we are open to different layouts for the page design (as long as they capture the information effectively and making it easy to understand).

Target Market(s)

Potential Home owners, Families and Business Owners

Industry/Entity Type

Business

Requirements
Must have
• - Must contain our logo (attached as PNG and Illustrator file)
- Winning designer must supply a Photoshop file (PSD) that will allow us.
Nice to have
• - Should include photos/images of families, professional groups, tradespeople etc (you can use stock photos from PixQuarry and I will purchase them once you are selected as the winning design)
- Link to a loan calculator somewhere on front page with a button 'Find out how much you could borrow' (or maybe even try adding a loan calculator to the homepage if you think this would look good)
- Page should have a main headline "Finding the right loan for you" or "Brightwell Lending finds the right loan for our customers."
- Must include Accreditation logos somewhere on the homepage (will try and supply these soon)
Should not have
• - Poor quality designs will not be considered
- Do not use clipart

```html
<!DOCTYPE html>
<html lang="en">
<head>
<meta charset="utf-8">
<title>Brightwell Lending</title>
<link href="https://fonts.googleapis.com/css2?family=Open+Sans:wght@400;600&family=Arimo:wght@400&display=swap" rel="stylesheet">
<style>
:root{
  --cyan:#2eade3;
  --blue:#004b70;
  --navy:#0a4a72;
  --white:#ffffff;
  --band:#f1f1f1;
  --rule:#d6d6d6;
  --text:#555555;
  --dark:#222222;
}
*{margin:0;padding:0;box-sizing:border-box}
html,body{width:1007px;height:1200px;overflow:hidden;background:var(--white)}
body{position:relative;font-family:"Arimo",Arial,sans-serif;color:var(--text)}
.abs{position:absolute}
.topbar{left:0;top:0;width:1007px;height:15px;background:linear-gradient(#0f5f8a,#0a4d74)}
.header{left:0;top:15px;width:1007px;height:97px;background:linear-gradient(#ffffff,#f4f4f4);box-shadow:0 2px 3px rgba(0,0,0,.12)}
.brand{left:90px;top:78px;display:flex;align-items:center;gap:8px;font-family:"Open Sans",sans-serif;font-weight:600;font-size:21px;line-height:28px;color:var(--cyan);letter-spacing:-.3px}
.brand-dot{width:14px;height:14px;border-radius:50%;background:var(--blue)}
.phone{left:760px;top:30px;display:flex;align-items:center;gap:6px;font-family:"Open Sans",sans-serif;font-size:20px;color:#666}
.phone svg{width:21px;height:21px}
.nav a{position:absolute;top:79px;height:28px;line-height:28px;font-family:"Open Sans",sans-serif;font-size:17.5px;color:var(--dark);text-decoration:none}
.nav .active{left:431px;width:90px;background:var(--blue);color:var(--white);text-align:center}
.nav .sep{position:absolute;top:79px;width:1px;height:28px;background:var(--rule)}
.hero{left:0;top:112px;width:1007px;height:330px;
  background:
    linear-gradient(180deg,rgba(11,86,128,0) 70%,rgba(11,86,128,.35) 100%),
    linear-gradient(90deg,#0b5680 0%,#2c6e94 9%,#c9d8e3 20%,#eef2f5 34%,#f6f7f8 50%,#e4ebf0 66%,#8fb0c6 80%,#1e6690 91%,#0b5680 100%)}
.services{left:0;top:442px;width:1007px;height:239px;background:var(--band);box-shadow:inset 0 -6px 6px -4px rgba(0,0,0,.08)}
.col-rule{top:456px;width:1px;height:209px;background:var(--rule)}
.svc-title{top:487px;display:flex;align-items:center;gap:7px;font-family:"Open Sans",sans-serif;font-size:16px;color:var(--blue)}
.svc-title svg{width:18px;height:18px}
.svc-list{list-style:none;font-size:12px;color:var(--dark)}
.svc-list li{height:22px;line-height:14px;padding-left:15px;position:relative;white-space:nowrap}
.svc-list li::before{content:"";position:absolute;left:1px;top:4px;width:5px;height:5px;background:var(--cyan);transform:rotate(45deg)}
.btn{top:610px;width:79px;height:28px;border:1px solid #c8c8c8;border-radius:3px;background:linear-gradient(#ffffff,#e9e9e9);box-shadow:0 1px 2px rgba(0,0,0,.12);font-size:10.5px;color:#555;text-align:center;line-height:26px}
.welcome h1{position:absolute;left:99px;top:706px;font-family:"Open Sans",sans-serif;font-weight:400;font-size:20px;color:var(--blue)}
.copy{left:100px;top:747px;width:830px;font-size:12.1px;line-height:16.8px;color:var(--text)}
.copy p{margin-bottom:16.8px}
.calc{left:100px;top:975px;width:236px;height:112px;border:1px solid #cfcfcf;border-radius:3px;background:linear-gradient(#ffffff,#ececec)}
.calc-art{position:absolute;left:12px;top:20px;width:76px;height:62px;border-radius:4px;background:linear-gradient(135deg,#9aa6ae,#5e6a72 60%,#c9ced2)}
.calc-text{position:absolute;left:100px;top:20px;width:124px;text-align:center;font-family:"Open Sans",sans-serif;font-size:16px;line-height:22px;color:var(--blue)}
.divider{left:362px;top:971px;width:1px;height:126px;background:var(--rule)}
.accred-title{left:388px;top:970px;font-family:"Open Sans",sans-serif;font-size:17px;color:var(--blue)}
.badge-a{left:388px;top:998px;width:100px;height:91px;border-radius:6px;background:var(--navy)}
.badge-b{left:518px;top:1000px;width:89px;height:87px;border-radius:6px;background:#8e1a55}
.badge-c{left:633px;top:1000px;width:210px;height:88px;border:3px solid #1c5aa6;border-radius:44px}
.badge-c::before{content:"";position:absolute;left:6px;top:6px;width:70px;height:70px;border-radius:50%;background:#1c5aa6}
.footer{left:0;top:1106px;width:1007px;height:94px;background:var(--band);font-size:10.5px;color:var(--dark);text-align:center}
.footer .links{position:absolute;top:25px;width:100%}
.footer .links a{color:var(--dark);text-decoration:none}
.footer .links a.current{color:var(--blue)}
.footer .legal{position:absolute;top:44px;width:100%}
.footer .credit{position:absolute;top:63px;width:100%}
</style>
</head>
<body>
<div class="abs topbar"></div>
<header class="abs header"></header>
<div class="abs brand"><span class="brand-dot"></span>Brightwell Lending</div>
<div class="abs phone">
  <svg viewBox="0 0 24 24"><circle cx="12" cy="12" r="12" fill="#2eade3"/><path d="M8 6c1 0 2 2.5 2 3s-1 1-1 1.6c.6 1.6 2 3 3.4 3.4.6 0 1-1 1.6-1s3 1 3 2-1.5 2-2.5 2C10 17.5 6.5 14 6.5 8.5 6.5 7.5 7 6 8 6z" fill="#fff"/></svg>
  1800 555 214
</div>
<nav class="nav">
  <a class="active" href="#">Home</a>
  <a href="#" style="left:540px">Services</a>
  <span class="sep" style="left:625px"></span>
  <a href="#" style="left:646px">About Us</a>
  <span class="sep" style="left:736px"></span>
  <a href="#" style="left:760px">Faq</a>
  <span class="sep" style="left:801px"></span>
  <a href="#" style="left:830px">Contact Us</a>
</nav>

<div class="abs hero" role="img" aria-label="Photo of a smiling professional team giving thumbs up, fading into blue at both sides"></div>

<section class="abs services"></section>
<span class="abs col-rule" style="left:245px"></span>
<span class="abs col-rule" style="left:459px"></span>
<span class="abs col-rule" style="left:657px"></span>

<div class="abs svc-title" style="left:101px">
  <svg viewBox="0 0 18 18"><path d="M2 9l7-6 7 6" fill="none" stroke="#555" stroke-width="1.6"/><rect x="4" y="9" width="10" height="7" fill="#dcdcdc" stroke="#777"/><rect x="7.5" y="11" width="3" height="5" fill="#2eade3"/></svg>Home loans</div>
<ul class="abs svc-list" style="left:101px;top:527px"><li>Home buyers</li><li>First home buyers</li><li>Over 20 lenders</li></ul>
<div class="abs btn" style="left:111px">Read More</div>

<div class="abs svc-title" style="left:278px">
  <svg viewBox="0 0 18 18"><circle cx="7" cy="11" r="5" fill="#e0b23a"/><circle cx="12" cy="6" r="4" fill="#f0cb5a"/></svg>Investment loans</div>
<ul class="abs svc-list" style="left:276px;top:528px"><li>Property investment loans</li><li>Interest only loans</li></ul>
<div class="abs btn" style="left:277px;top:609px">Read More</div>

<div class="abs svc-title" style="left:484px">
  <svg viewBox="0 0 18 18"><ellipse cx="9" cy="14" rx="7" ry="2.5" fill="#c9962a"/><ellipse cx="9" cy="10" rx="7" ry="2.5" fill="#dcaa35"/><ellipse cx="9" cy="6" rx="7" ry="2.5" fill="#f0c452"/></svg>Business loans</div>
<ul class="abs svc-list" style="left:485px;top:527px"><li>Long term</li><li>Short term</li><li>Equipment &amp; Leasing</li></ul>
<div class="abs btn" style="left:486px">Read More</div>

<div class="abs svc-title" style="left:696px">
  <svg viewBox="0 0 18 18"><circle cx="9" cy="5" r="3.5" fill="#8a6a4a"/><path d="M3 17c0-5 3-7 6-7s6 2 6 7z" fill="#2f7d3a"/></svg>Refinancing loans</div>
<ul class="abs svc-list" style="left:697px;top:527px"><li>Refinancing for the best rate</li><li>Upsizing or downsizing</li><li>Change from a variable to a fixed rate</li></ul>
<div class="abs btn" style="left:697px">Read More</div>

<section class="welcome">
  <h1>Welcome to Brightwell Lending</h1>
  <div class="abs copy">
    <p>At Brightwell Lending we work hard to find the right loan for our customers. We do that because we are backed by sound industry knowledge, professional experience and a great customer service approach.</p>
    <p>Brightwell Lending guarantees that we will always tailor the best solution for your individual lending needs.</p>
    <p>We can do that because we have access to a wide variety of lending options from major banks to non-bank lenders and we are committed to finding the right lending product for you.</p>
    <p>There are many different loan products in the marketplace. Brightwell Lending has access to a wide panel of lenders which means we can access bank and non-bank lenders that meet the individual needs of our customers.</p>
    <p>Contact Brightwell Lending today on: 1800 555 214 to find out more.</p>
  </div>
</section>

<div class="abs calc">
  <div class="calc-art" role="img" aria-label="Illustration of a model house on a calculator"></div>
  <div class="calc-text">Find out how much you could borrow</div>
</div>
<span class="abs divider"></span>
<div class="abs accred-title">Accreditation logos</div>
<div class="abs badge-a" role="img" aria-label="Broker association accreditation badge"></div>
<div class="abs badge-b" role="img" aria-label="Accredited company badge"></div>
<div class="abs badge-c" role="img" aria-label="Accredited financial planning firm badge"></div>

<footer class="abs footer">
  <div class="links"><a class="current" href="#">Home</a> &nbsp;|&nbsp; <a href="#">Services</a> &nbsp;|&nbsp; <a href="#">About Us</a> &nbsp;|&nbsp; <a href="#">Faq</a> &nbsp;|&nbsp; <a href="#">Contact Us</a></div>
  <div class="legal">Copyright © 2012 Brightwell Lending. All Rights Reserved. &nbsp;|&nbsp; Sitemap</div>
  <div class="credit">Powered by Pixel &amp; Pine</div>
</footer>
</body>
</html>
```